Introducting Corbin Sheetmetal MADE WITH PRIDE

We require a PDF fact sheet that we can share via email that has a summary of infomation, services and products as found on our website www.corbinsheetmetal.example

The Call to Action - Heading should be "Made with Pride"

Needs to look professional, prefer sharp lines than bubble circles

Trying to attract new business

Target Market(s)

Potential new clients; Plumbers, Shop fitters, restaurants and Caters.

Industry/Entity Type

Manufacturing

Font styles to use
Other font styles liked:
• something masculine

Colors

Designer to choose colors to be used in the design.

Requirements
Must have
• Must be one page, low res so when emailing it's not too large.
• Must have phone number, email address and actual address
• Should include summary of copy from the website; www.corbinsheetmetal.example
• * A bit about us
• * Services
• * Fabrication Range and Finishes
• * General Fabrication
Nice to have
• Something that is not too busy, easy to read - so not too much writing. Must look professional (that's why we using ArtHive).
• Please let me know I you need images from the website and I'll sent to you.
Should not have
• It shouldn't be too busy, easy to read - so not too much writing. Simple and clear message.

```html
<!DOCTYPE html>
<html lang="en">
<head>
<meta charset="utf-8">
<title>Corbin Sheetmetal – Made With Pride</title>
<link href="https://fonts.googleapis.com/css2?family=Montserrat:wght@400;500;600;700;800&display=swap" rel="stylesheet">
<style>
:root{
  --backdrop:#a7a7a7;
  --paper:#ffffff;
  --ink:#1f1f1f;
  --charcoal-top:#58575a;
  --charcoal-bottom:#3e3d40;
  --sky:#4fb8ec;
  --azure:#3f8fdc;
  --royal:#4a6fd0;
  --soft-white:#f2f2f2;
}
*{margin:0;padding:0;box-sizing:border-box}
html,body{width:1200px;height:1200px;overflow:hidden}
body{background:var(--backdrop);font-family:"Montserrat",sans-serif;color:var(--ink);position:relative}
.sheet{position:absolute;left:162px;top:33px;width:877px;height:1134px;background:var(--paper)}
.block{position:absolute}

/* header */
.brand{left:0;top:0;width:305px;height:136px;display:flex;align-items:center;justify-content:center;gap:10px}
.brand-mark{width:14px;height:14px;background:#6d6e71}
.brand-name{font-size:17px;font-weight:600;letter-spacing:1.5px;color:#3a3a3c;text-transform:uppercase}
.pride{left:305px;top:0;width:281px;height:136px;background:linear-gradient(100deg,var(--royal) 0%,var(--azure) 45%,var(--sky) 100%);color:#fff;text-align:center;padding-top:40px}
.pride-small{font-size:23px;font-weight:800;letter-spacing:1px;line-height:1}
.pride-big{font-size:47px;font-weight:800;letter-spacing:1px;line-height:.95}
.contact{left:586px;top:22px;width:290px}
.contact-row{display:flex;align-items:center;gap:8px;font-size:12.5px;line-height:14px;margin-bottom:11px;color:#2a2a2a}
.contact-row svg{flex:0 0 26px}

/* photos */
.photo{top:139px;height:274px}
.photo-cabinet{left:0;width:302px;background:linear-gradient(120deg,#2d4db8 0%,#2443a8 45%,#7a7468 80%,#c9b89a 100%)}
.photo-welder{left:305px;width:281px;background:linear-gradient(135deg,#6c6a5c 0%,#b7b93a 35%,#4f3a30 65%,#8a8c90 100%)}
.photo-pipes{left:589px;width:288px;background:linear-gradient(100deg,#bfbdb8 0%,#2a3a8e 45%,#d4d2cc 75%,#9a9893 100%)}

/* dark panel */
.panel{left:0;top:417px;width:586px;height:541px;background:linear-gradient(180deg,var(--charcoal-top),var(--charcoal-bottom));color:var(--soft-white)}
.col{position:absolute;top:37px;font-size:15.2px;line-height:19px;letter-spacing:.3px}
.col-services{left:28px;width:260px}
.col-materials{left:333px;width:240px}
.divider{position:absolute;left:301px;top:37px;width:2px;height:472px;background:#e8e8e8}
.section-title{font-size:15px;font-weight:600;letter-spacing:.8px;text-transform:uppercase;line-height:18px}
.panel .section-title{color:var(--sky)}
.rule{width:58px;height:3px;margin:16px 0 22px}
.panel .rule{background:#fff}
.lead-hi{color:var(--sky);font-weight:600}
.lead-b{font-weight:600}
.col p{margin-bottom:19px}
.col ul{list-style:none;margin-bottom:19px}
.col li{padding-left:17px;position:relative}
.col li::before{content:"•";position:absolute;left:0}

/* about */
.about{left:614px;top:437px;width:240px}
.about .rule{background:var(--sky);margin:17px 0 22px}
.about-copy{font-size:15.6px;line-height:18.9px;color:#1f1f1f}
.about-copy b{font-weight:700}

/* bottom */
.fabrication{left:28px;top:979px;width:540px}
.fabrication .rule{background:var(--sky);margin:15px 0 23px}
.fab-copy{font-size:15.2px;line-height:19px;letter-spacing:.2px}
.fab-copy b{font-weight:700}
.cta{left:589px;top:961px;width:288px;height:173px;background:linear-gradient(135deg,var(--royal) 0%,var(--azure) 50%,var(--sky) 100%)}
.cta-frame{position:absolute;left:32px;top:24px;width:224px;height:127px;border:2px solid #fff;color:#fff;text-align:center}
.cta-title{font-size:24px;font-weight:600;letter-spacing:1px;margin-top:15px}
.cta-line{width:58px;height:2px;background:#fff;margin:12px auto 14px}
.cta-phone{font-size:25px;font-weight:600;letter-spacing:.5px}
</style>
</head>
<body>
<main class="sheet">
  <header>
    <div class="block brand">
      <span class="brand-mark"></span>
      <span class="brand-name">Corbin Sheetmetal</span>
    </div>
    <div class="block pride">
      <div class="pride-small">MADE WITH</div>
      <div class="pride-big">PRIDE</div>
    </div>
    <div class="block contact">
      <div class="contact-row">
        <svg width="26" height="26" viewBox="0 0 26 26"><circle cx="13" cy="13" r="13" fill="#4fb8ec"/><path d="M7 13 L13 7.5 L19 13 M9 12 V18.5 H17 V12" fill="none" stroke="#fff" stroke-width="2"/><rect x="11.5" y="14.5" width="3" height="4" fill="#fff"/></svg>
        <span>14 Halden St, Kestrel Park<br>SA 5999, Australia</span>
      </div>
      <div class="contact-row">
        <svg width="26" height="26" viewBox="0 0 26 26"><circle cx="13" cy="13" r="13" fill="#4fb8ec"/><rect x="7" y="9" width="12" height="8.5" fill="none" stroke="#fff" stroke-width="1.6"/><path d="M7 9 L13 14 L19 9" fill="none" stroke="#fff" stroke-width="1.6"/></svg>
        <span>info@corbinsheetmetal.example</span>
      </div>
      <div class="contact-row">
        <svg width="26" height="26" viewBox="0 0 26 26"><circle cx="13" cy="13" r="13" fill="#4fb8ec"/><path d="M9 7 C7.5 8 7.5 11 9.5 14.5 C11.5 18 14.5 20 16.5 19.5 L17.5 17.5 L15 15.5 L13.8 16.5 C12.6 15.8 11 13.5 10.6 12 L11.8 11 L10.5 7.8 Z" fill="#fff"/></svg>
        <span>(08) 5550 1947</span>
      </div>
    </div>
  </header>

  <div class="block photo photo-cabinet" role="img" aria-label="Blue fabricated steel equipment cabinet in a workshop"></div>
  <div class="block photo photo-welder" role="img" aria-label="Tradesperson in hi-vis vest welding a steel pipe"></div>
  <div class="block photo photo-pipes" role="img" aria-label="Steel frame holding blue filter tanks with white pipework"></div>

  <section class="block panel">
    <div class="col col-services">
      <h2 class="section-title">Services</h2>
      <div class="rule"></div>
      <p><span class="lead-hi">We can produce</span> <span class="lead-b">and supply</span> a range of sheet metal components for all industries.</p>
      <p><span class="lead-hi">We can assist</span> <span class="lead-b">with a range of</span> sheetmetal products using years of experience and a range of equipment.</p>
      <ul>
        <li>Commercial kitchen canopies</li>
        <li>Shelvng</li>
        <li>Tanks</li>
        <li>Silt traps</li>
        <li>Bench tops</li>
        <li>Safety trays</li>
        <li>Tundishes</li>
        <li>Hand rails</li>
        <li>Brackets</li>
        <li>Mild Steel / Frame Work</li>
        <li>Duct Work</li>
        <li>Most Stainless Steel components</li>
      </ul>
    </div>
    <div class="divider"></div>
    <div class="col col-materials">
      <h2 class="section-title">Materials and Finishes</h2>
      <div class="rule"></div>
      <p><span class="lead-hi">We fabricate</span> <span class="lead-b">a range of</span> materials including:</p>
      <ul>
        <li>Stainless Steel</li>
        <li>Aluminium</li>
        <li>Galvanised</li>
        <li>Brass</li>
        <li>Mild Steel</li>
      </ul>
      <p><span class="lead-hi">Finishes</span> <span class="lead-b">include:</span></p>
      <ul>
        <li>Polished</li>
        <li>Powder-Coated</li>
        <li>Painted</li>
        <li>Mirrored</li>
        <li>Textured</li>
      </ul>
      <p><span class="lead-hi">We have</span> <span class="lead-b">experienced</span> tradespeople with extensive experience and abilities to custom fabricate to your specific design.</p>
    </div>
  </section>

  <section class="block about">
    <h2 class="section-title">A Bit About Us</h2>
    <div class="rule"></div>
    <p class="about-copy"><b>Fast, friendly, and fully</b> functional, our professional Metal Fabrication Service is well renowned throughout South Australia. Our team is up for every job, managing projects with the skill and experience our clients have come to expect. We always stand behind our work, custom made with pride. Established in 1991, we are suppliers to the plumbing and mining trades, shop-fitters and builders, and the general public. We provide general sheetmetal and light steel fabrication services (cutting, folding, mig/tig welding) working with stainless steel, copper, galvanised steel, aluminium and mild steel.</p>
  </section>

  <section class="block fabrication">
    <h2 class="section-title">General Fabrication</h2>
    <div class="rule"></div>
    <p class="fab-copy"><b>Wether you’re performing</b> shop fabrication, repairing equipment on a farm or job site, or creating artwork in your garage, Corbin Sheetmetal has the knowhow, creativity and process knowledge to help you get your job done right.</p>
  </section>

  <aside class="block cta">
    <div class="cta-frame">
      <div class="cta-title">CALL US</div>
      <div class="cta-line"></div>
      <div class="cta-phone">(08) 5550 1947</div>
    </div>
  </aside>
</main>
</body>
</html>
```